Book cover for a book on tactics, habits and directives learned from world class performers

The Quiet Ledger book is the first in a series of four books filled with proven tactics, habits and directives (i.e., what to do) that young, ambitious working professionals should be doing to make their life better. The first book is on foundational or keystone habits - that is, the habits that will help everyone upgrade their life and enable other great habits in their life (things such as waking up early in the morning or exercising)

The goal of the book is to stand out on the Brimvale platform as a small thumbnail, as well as a 5 x 8 book.

The imagery should make the viewer feel that the book (and the author) are the authority in habits and developing habits.

The reader should feel that they must have this book if they know they should be developing successful habits but do not want to comb through hundreds of books just to find the one tactic or habit that they should be doing. It's important that the book "pops off the shelf" and catches the eye quickly.

The most important part of the design is that it sells, not that it looks well-designed. I am open to any image or illustration you choose though please consider the nice have I have listed below. Here are a few words that come to mind when thinking of my book: growth, self development, leadership, success, freedom, passion, motivation, young professional, accomplished, experience.

I like a bold color palette. I like bold titles that you know right away what the title is and what it is about, not too busy and with simple color schemes. 2 - 3 colors.

Books with covers I like:
- Lamp Orchard by Norris Pellaquin
- Under The Copper Tide by Gordon Pruitt
- The Velvet Compass by Edgar Fulbright

Target Market(s)

- Young 20 - 40 year old ambitious working professionals interested in self development and listen to podcasts of Ned Caplow, Rufus Denholme
- Just starting out management consultants

Colors

Designer to choose colors to be used in the design.

Requirements
Must have
• 'Quiet Ledger' title - first and foremost
• Author name - Lu Qiao - probably on the bottom or somewhere
• Bold colour / colours or a graphic that is eye catching (and makes it different from other habits books on Brimvale)
Nice to have
• Would like to have some sort of visual, colour or theme that can run through the four books - would be great to have a cover design that can be simply changed to depict the second, third or fourth book in the series - maybe the graphic or visual can be changed with some colours, etc. but with the overall feel looking similar so that people can see that it's part of the same book series

```html
<!DOCTYPE html>
<html lang="en">
<head>
<meta charset="utf-8">
<title>Quiet Ledger — Lu Qiao</title>
<link rel="stylesheet" href="https://fonts.googleapis.com/css2?family=Bebas+Neue&family=Poppins:wght@700&display=swap">
<style>
  :root {
    --stage: #ffffff;
    --cover-green: #24a94a;
    --band-green: #14944a;
    --ink-white: #ffffff;
  }
  * { margin: 0; padding: 0; box-sizing: border-box; }
  html, body {
    width: 1200px;
    height: 1200px;
    overflow: hidden;
    background: var(--stage);
  }
  .book-cover {
    position: absolute;
    left: 253px;
    top: 50px;
    width: 693px;
    height: 1100px;
    background: var(--cover-green);
    overflow: hidden;
  }
  .title {
    position: absolute;
    left: 0;
    right: 0;
    text-align: center;
    color: var(--ink-white);
    font-family: "Bebas Neue", "Oswald", sans-serif;
    font-weight: 400;
    line-height: 1;
  }
  .title-top {
    top: 124px;
    font-size: 112px;
    letter-spacing: 4px;
  }
  .title-main {
    top: 240px;
    font-size: 232px;
    letter-spacing: 10px;
  }
  .habit-ring {
    position: absolute;
    left: 0;
    top: 0;
    width: 693px;
    height: 1100px;
  }
  .author-band {
    position: absolute;
    left: 0;
    top: 0;
    width: 693px;
    height: 1100px;
  }
  .author-name {
    position: absolute;
    left: 0;
    right: 0;
    top: 1052px;
    text-align: center;
    color: var(--ink-white);
    font-family: "Poppins", "Arial", sans-serif;
    font-weight: 700;
    font-size: 23px;
    letter-spacing: 4px;
    line-height: 1;
  }
</style>
</head>
<body>
  <main class="book-cover">
    <h1>
      <span class="title title-top">QUIET</span>
      <span class="title title-main">LEDGER</span>
    </h1>

    <svg class="habit-ring" viewBox="0 0 693 1100" role="img" aria-label="Ring of six white discs holding habit pictograms: reading, running, stretching, meditating, sleeping and standing">
      <circle cx="347" cy="725" r="182" fill="none" stroke="var(--ink-white)" stroke-width="3"/>
      <g fill="var(--ink-white)">
        <circle cx="279" cy="561" r="55"/>
        <circle cx="455" cy="581" r="55"/>
        <circle cx="523" cy="740" r="55"/>
        <circle cx="417" cy="886" r="55"/>
        <circle cx="232" cy="866" r="55"/>
        <circle cx="169" cy="699" r="55"/>
      </g>
    </svg>

    <svg class="author-band" viewBox="0 0 693 1100" aria-hidden="true">
      <polygon points="225,1034 472,1034 504,1100 193,1100" fill="var(--band-green)"/>
    </svg>
    <p class="author-name">LU QIAO</p>
  </main>
</body>
</html>
```